Solar Company Bussiness Card

I need a 2 sided business card and would like a .psd and any font files for each side of the card. I would like my logo used, it should be attached with the fonts. I'm not opposed to the font colors with the logo being changed.

On the sample design, I'd like the following:

Darren Pellow
President
Phone: 555-318-2947
www.sunvaleenergyco.example

As I've recently opened in a 2nd market, I'm not sure about an address as I currently have 2 of them. I may actually get separate cards printed, one batch for each address, that's why I need the PSD file.
Updates

I'm very pleased with the response and designs I've received here for my business card. First and foremost, I'd like to thank everyone who took the time to submit a design. There truly are a lot of great designs in the bunch here and I'm having a little difficulty deciding. I will be reaching out to someone in the next day or two here to go to a final design. At this time, I'm not looking for any new concepts. If any of you do logos, I'm looking for a new logo for our sister entity, Pellow Partners, Inc. Thanks, Darren Pellow

Reason: I'm not looking for any new designs at this point, but extending this deadline in order to give people I've asked a chance to re-submit items.

Industry/Entity Type

Business

```html
<!DOCTYPE html>
<html lang="en">
<head>
<meta charset="utf-8">
<title>Sunvale Energy Co. – Business Card</title>
<link rel="stylesheet" href="https://fonts.googleapis.com/css2?family=Open+Sans:wght@400;600;700&display=swap">
<style>
  :root {
    --page-bg: #e9eaec;
    --card-bg: #ffffff;
    --card-shade: #f1f2f4;
    --brand-blue: #1d5fa8;
    --accent-blue: #1aa0e6;
    --swoosh-light: #1e93e4;
    --swoosh-deep: #2a52b8;
    --swoosh-dark: #2f3136;
    --text-dark: #2b2d31;
    --text-mid: #45484e;
  }
  * { box-sizing: border-box; margin: 0; padding: 0; }
  html, body {
    width: 1200px; height: 900px; overflow: hidden;
    background: var(--page-bg);
    font-family: "Open Sans", Arial, sans-serif;
  }
  .business-card {
    position: absolute; left: 150px; top: 193px;
    width: 900px; height: 514px;
    border-radius: 40px; overflow: hidden;
    background: radial-gradient(ellipse at 45% 55%, var(--card-bg) 40%, var(--card-shade) 100%);
    box-shadow: 0 10px 30px rgba(0,0,0,0.12);
  }
  .card-swoosh { position: absolute; inset: 0; width: 900px; height: 514px; }
  .brand {
    position: absolute; left: 72px; top: 140px;
    display: flex; align-items: center; gap: 14px;
    white-space: nowrap;
  }
  .brand-mark { width: 30px; height: 30px; background: var(--brand-blue); flex: none; }
  .brand-name {
    font-weight: 600; font-size: 36px; color: var(--brand-blue);
    letter-spacing: -0.5px; line-height: 1;
  }
  .contact-person {
    position: absolute; left: 520px; top: 166px;
    white-space: nowrap;
  }
  .person-name {
    font-weight: 700; font-size: 21px; color: var(--accent-blue);
    letter-spacing: 0.5px; text-transform: uppercase; line-height: 1.2;
  }
  .person-title { font-size: 18px; color: var(--text-dark); margin-top: 2px; }
  .address {
    position: absolute; left: 80px; top: 262px;
    font-size: 21px; line-height: 1.5; color: var(--text-dark);
  }
  .contact-list {
    position: absolute; left: 84px; top: 368px;
    list-style: none; font-size: 19px; color: var(--text-mid);
  }
  .contact-item { display: flex; align-items: center; gap: 14px; height: 30px; }
  .contact-icon { width: 18px; height: 18px; flex: none; }
</style>
</head>
<body>
  <article class="business-card">
    <svg class="card-swoosh" viewBox="0 0 900 514" aria-hidden="true">
      <defs>
        <linearGradient id="swooshBlue" x1="0" y1="0" x2="1" y2="1">
          <stop offset="0" stop-color="var(--swoosh-light)"/>
          <stop offset="1" stop-color="var(--swoosh-deep)"/>
        </linearGradient>
      </defs>
      <path d="M600 0 C860 40 930 330 690 514 L900 514 L900 0 Z" fill="url(#swooshBlue)"/>
      <path d="M620 0 L900 0 L900 175 C860 85 770 22 620 0 Z" fill="var(--swoosh-dark)"/>
    </svg>

    <div class="brand">
      <span class="brand-mark"></span>
      <span class="brand-name">Sunvale Energy Co.</span>
    </div>

    <div class="contact-person">
      <p class="person-name">Marcus Hale</p>
      <p class="person-title">Managing Director</p>
    </div>

    <p class="address">204 Harbor Point, Suite 12<br>Linden Row Road</p>

    <ul class="contact-list">
      <li class="contact-item">
        <svg class="contact-icon" viewBox="0 0 24 24"><path fill="var(--accent-blue)" d="M6.6 10.8a15.1 15.1 0 0 0 6.6 6.6l2.2-2.2a1 1 0 0 1 1-.25 11.4 11.4 0 0 0 3.6.57 1 1 0 0 1 1 1V20a1 1 0 0 1-1 1A17 17 0 0 1 3 4a1 1 0 0 1 1-1h3.5a1 1 0 0 1 1 1c0 1.25.2 2.450.57 3.57a1 1 0 0 1-.25 1z"/></svg>
        <span>555-204-7731</span>
      </li>
      <li class="contact-item">
        <svg class="contact-icon" viewBox="0 0 24 24"><rect x="2" y="5" width="20" height="14" rx="1.5" fill="var(--accent-blue)"/><path d="M3 6l9 7 9-7" fill="none" stroke="#fff" stroke-width="1.6"/></svg>
        <span>hello@sunvaleenergy.example</span>
      </li>
      <li class="contact-item">
        <svg class="contact-icon" viewBox="0 0 24 24"><g fill="none" stroke="var(--accent-blue)" stroke-width="2"><circle cx="12" cy="12" r="9.5"/><ellipse cx="12" cy="12" rx="4" ry="9.5"/><path d="M2.5 12h19M4 7h16M4 17h16"/></g></svg>
        <span>www.sunvaleenergyco.example</span>
      </li>
    </ul>
  </article>
</body>
</html>
```